Online Marketing Agency Website

We are an online marketing agency that specializes in search marketing (SEM) for businesses of all sizes. Our core services include local search marketing, seo, paid search, paid social, graphic design, video production/editing and website design. We have an existing website that we launched a number of years ago but it's very outdated and we're currently too busy to design a new version.

Target Market(s)

Any business that needs online marketing services with an emphasis on search marketing.

Industry/Entity Type

Ad Agency

Number of Pages Required

4 page

Font styles to use
Sans Serif

Requirements
Must have
• Home page, interior page, blog page, contact us page.
Look and feel should be modern and clean and easy to navigate.
Sections for call outs for specific services: Business Marketing Strategy, Content Creation and Marketing, Graphic & Publication Design, Pay Per Click (PPC) Management, Search Engine Optimization, Social Media Management, Video Production & Editing, Website Hosting & Management, Website Design & Development
Use color from logo that was uploaded.

```html
<!DOCTYPE html>
<html lang="en">
<head>
<meta charset="utf-8">
<title>Summit Digital — Online Marketing. Elevated</title>
<link rel="stylesheet" href="https://fonts.googleapis.com/css2?family=Anton&family=Montserrat:wght@400;500;600;700&display=swap">
<style>
:root{
  --orange:#ff4f0f;
  --orange-dark:#c93c08;
  --orange-deep:#b53405;
  --ink:#111111;
  --text:#555555;
  --muted:#8a8a8a;
  --line:#dddddd;
  --white:#ffffff;
  --footer:#070707;
}
*{margin:0;padding:0;box-sizing:border-box}
html,body{width:1200px;height:4167px;overflow:hidden}
body{font-family:"Montserrat",sans-serif;color:var(--text);background:var(--white);position:relative}
.abs{position:absolute}

/* top bar */
.topbar{left:0;top:0;width:1200px;height:31px;background:var(--orange);color:var(--white);font-size:11px}
.topbar .mail{left:692px;top:8px;display:flex;align-items:center;gap:8px}
.topbar .phone{left:910px;top:5px;font-size:16px;display:flex;align-items:center;gap:8px}

/* nav */
.navbar{left:0;top:31px;width:1200px;height:69px;background:var(--white)}
.brand{left:160px;top:20px;display:flex;align-items:center;gap:8px}
.brand .dot{width:22px;height:22px;border-radius:50%;background:var(--orange)}
.brand .name{font-size:13px;font-weight:700;color:var(--ink);letter-spacing:.3px}
.nav{left:656px;top:30px;display:flex;gap:38px;font-size:11px;color:#444;list-style:none}
.nav .active{color:var(--orange);display:flex;align-items:center;gap:6px}
.nav .active::before{content:"";width:7px;height:7px;border-radius:50%;background:var(--orange)}

/* hero */
.hero-photo{left:0;top:100px;width:1200px;height:631px;background:linear-gradient(120deg,#1d1f24 0%,#3a3e46 45%,#6c7380 70%,#2b2d31 100%)}
.hero-shade{left:0;top:100px;width:1200px;height:631px;background:radial-gradient(ellipse at 50% 45%,rgba(0,0,0,.15),rgba(0,0,0,.55))}
.hero-wedge{left:0;top:640px}
.hero-copy{left:0;top:247px;width:1200px;text-align:center;color:var(--white)}
.eyebrow{font-size:14px;font-weight:500;color:var(--orange);letter-spacing:.3px}
.hero-title{font-family:"Anton",sans-serif;font-size:64px;line-height:66px;margin-top:18px;letter-spacing:1px}
.hero-sub{font-size:15px;margin-top:16px}
.btn{display:inline-flex;align-items:center;gap:14px;background:var(--orange);color:var(--white);font-weight:600;font-size:15px;height:40px;padding:0 4px 0 22px;border-radius:20px}
.btn .knob{width:32px;height:32px;border-radius:50%;background:var(--white);display:flex;align-items:center;justify-content:center}
.hero-copy .btn{margin-top:28px}

/* welcome */
.welcome{left:0;top:810px;width:1200px;text-align:center}
.welcome .kicker{font-size:17px;font-weight:600;color:var(--ink)}
.section-title{font-size:34px;font-weight:600;color:var(--ink);letter-spacing:.5px}
.section-title span{color:var(--orange)}
.welcome .section-title{margin-top:8px}
.welcome p{width:470px;margin:28px auto 0;font-size:12px;line-height:21px;color:var(--text)}
.welcome p+p{margin-top:14px}
.welcome .mark{width:80px;height:80px;border-radius:50%;background:var(--orange);margin:52px auto 0}

/* services band */
.services{left:0;top:1252px;width:1200px;height:441px;background:var(--orange)}
.services h2{position:absolute;left:0;top:72px;width:1200px;text-align:center;color:var(--white);font-weight:500;font-size:32px;line-height:38px}
.services .lead{position:absolute;left:350px;top:172px;width:500px;text-align:center;color:var(--white);font-size:12px;line-height:21px}
.service-row{position:absolute;left:0;top:278px;width:1200px;height:163px;display:flex}
.service{flex:1;background:var(--orange-dark);color:var(--white);text-align:center;font-size:13px;line-height:18px;padding-top:28px;position:relative}
.service:nth-child(odd){background:var(--orange-deep)}
.service.current{background:var(--orange)}
.service.current::after{content:"";position:absolute;left:50%;bottom:-12px;margin-left:-12px;border:12px solid transparent;border-bottom:0;border-top-color:var(--orange)}
.service svg{display:block;margin:0 auto 12px}

/* feature */
.feature-photo{left:0;top:1693px;width:1200px;height:631px;background:linear-gradient(180deg,#e6e6e6 0%,#d4d4d2 55%,#b89a73 80%,#9c7b55 100%)}
.feature-card{left:281px;top:2240px;width:638px;height:299px;background:var(--white);border-radius:8px;box-shadow:0 6px 20px rgba(0,0,0,.12);text-align:center}
.feature-card h3{font-size:23px;font-weight:500;color:var(--ink);margin-top:42px}
.feature-card p{width:440px;margin:22px auto 0;font-size:11px;line-height:20px;color:var(--text)}
.feature-card p+p{margin-top:12px}
.feature-card .btn{margin-top:18px}

/* blog */
.blog-title{left:0;top:2610px;width:1200px;text-align:center}
.post{top:2700px;width:270px}
.post .thumb{width:270px;height:195px;position:relative}
.post .date{position:absolute;left:28px;top:4px;width:45px;height:45px;background:var(--orange);color:var(--white);text-align:center;font-size:17px;font-weight:700;line-height:18px;padding-top:6px}
.post .date small{display:block;font-size:9px;font-weight:500;line-height:11px}
.post h4{font-size:13px;font-weight:500;color:var(--ink);line-height:23px;margin-top:26px}
.post p{font-size:11px;line-height:21px;color:var(--muted);margin-top:8px}
.post .rule{height:2px;background:var(--line);margin-top:22px;position:relative}
.post .rule::after{content:"";position:absolute;left:186px;top:0;width:62px;height:3px;background:var(--orange)}

/* contact */
.contact-photo{left:0;top:3165px;width:1200px;height:690px;background:linear-gradient(100deg,#5a5754 0%,#8a8681 40%,#a9a59f 70%,#6c6862 100%)}
.talk-circle{left:610px;top:3245px;width:426px;height:426px;border-radius:50%;background:var(--white)}
.talk-title{left:610px;top:3288px;width:426px;text-align:center;font-size:33px;font-weight:600;color:var(--ink)}
.talk-title span{color:var(--orange)}
.field{left:689px;width:268px;border:1px solid var(--line);background:var(--white);font-size:11px;color:#777;padding:8px 7px}
.talk-btn{left:727px;top:3573px}

/* footer */
.footer-wave{left:0;top:3760px}
.footer{left:0;top:3830px;width:1200px;height:337px;background:var(--footer);color:#bdbdbd}
.footer .f-brand{position:absolute;left:160px;top:56px;display:flex;align-items:center;gap:8px}
.footer .f-brand .dot{width:22px;height:22px;border-radius:50%;background:var(--orange)}
.footer .f-brand .name{font-size:14px;font-weight:700;color:#9a9a9a}
.footer .about{position:absolute;left:160px;top:131px;width:250px;font-size:11px;line-height:21px;color:#cfcfcf}
.socials{position:absolute;left:160px;top:206px;display:flex;gap:8px}
.socials span{width:32px;height:32px;border-radius:50%;background:var(--orange)}
.f-col{position:absolute;top:58px}
.f-col h5{font-size:15px;font-weight:500;color:var(--orange)}
.f-col ul{list-style:none;margin-top:20px;font-size:10px;line-height:22.5px;color:#cfcfcf}
.f-col li{display:flex;align-items:center;gap:12px}
.f-col li::before{content:"";width:4px;height:4px;border-radius:50%;background:var(--orange)}
.contact-list{list-style:none;margin-top:20px;font-size:10px;color:#cfcfcf}
.contact-list li{display:flex;gap:14px;line-height:16px;margin-bottom:16px}
.contact-list li::before{display:none}
.copyright{position:absolute;left:0;top:304px;width:1200px;text-align:center;font-size:10px;color:#cfcfcf}
</style>
</head>
<body>

<div class="abs topbar">
  <div class="abs mail">
    <svg width="13" height="10" viewBox="0 0 13 10"><rect x=".5" y=".5" width="12" height="9" fill="none" stroke="#fff"/><path d="M.5 .5l6 5 6-5" fill="none" stroke="#fff"/></svg>
    info@summitdigitalhq.com
  </div>
  <div class="abs phone">
    <svg width="15" height="15" viewBox="0 0 24 24"><path d="M6.6 10.8a15 15 0 006.6 6.6l2.2-2.2c.3-.3.7-.4 1-.2 1.1.4 2.3.6 3.6.6.6 0 1 .4 1 1V20c0 .6-.4 1-1 1A17 17 0 013 4c0-.6.4-1 1-1h3.5c.6 0 1 .4 1 1 0 1.3.2 2.5.6 3.6.1.3 0 .7-.2 1z" fill="#fff"/></svg>
    123 456 7890
  </div>
</div>

<header class="abs navbar">
  <div class="abs brand"><span class="dot"></span><span class="name">SUMMIT DIGITAL</span></div>
  <ul class="abs nav">
    <li class="active">HOME</li><li>ABOUT</li><li>INTERIOR</li><li>BLOG</li><li>CONTACT</li>
  </ul>
</header>

<div class="abs hero-photo" role="img" aria-label="Laptop on a desk showing a web analytics dashboard, with a coffee cup in the foreground"></div>
<div class="abs hero-shade"></div>
<svg class="abs hero-wedge" width="1200" height="100" viewBox="0 0 1200 100">
  <path d="M0 4 L600 91 L1200 4 L1200 100 L0 100Z" fill="#fff"/>
  <path d="M0 4 L600 91 L1200 0 L1200 32 L600 76 L0 38Z" fill="#ff4f0f"/>
</svg>
<div class="abs hero-copy">
  <div class="eyebrow">SUMMIT DIGITAL</div>
  <h1 class="hero-title">Online Marketing.<br>Elevated</h1>
  <p class="hero-sub">Summit Digital Is A Full-Service Online Marketing Agency</p>
  <span class="btn">CONTACT US<span class="knob"><svg width="14" height="14" viewBox="0 0 14 14"><path d="M7 1v12M2 6l5-5 5 5" fill="none" stroke="#ff4f0f" stroke-width="2"/></svg></span></span>
</div>

<section class="abs welcome">
  <div class="kicker">Welcome To</div>
  <h2 class="section-title">SUMMIT <span>DIGITAL</span></h2>
  <p>Lorem Ipsum is simply dummy text of the printing and typesetting industry. Lorem Ipsum has been the industry's standard dummy text ever since the 1500s, when an unknown printer.</p>
  <p>Lorem Ipsum is simply dummy text of the printing and typesetting industry. Lorem Ipsum has been the industry's standard dummy text ever since the 1500s, when an unknown printer took a galley of type and scrambled it to make a type specimen book. It has survived not only five centuries.</p>
  <div class="mark"></div>
</section>

<section class="abs services">
  <h2>Summit Digital is a Full–Service<br>Online Marketing Agency.</h2>
  <p class="lead">We can handle any element of your online marketing so you can get back to doing what you do best — growing your business. All of our services are offered on an 'a la carte' basis.</p>
  <div class="service-row">
    <div class="service"><svg width="44" height="40" viewBox="0 0 44 40" fill="none" stroke="#fff" stroke-width="1.5"><rect x="4" y="2" width="36" height="28"/><path d="M2 34h40M10 10l6 6M16 10l-6 6M28 20l6 4M14 22h6"/></svg>Business<br>Marketing<br>Strategy.</div>
    <div class="service current"><svg width="44" height="40" viewBox="0 0 44 40" fill="none" stroke="#fff" stroke-width="1.5"><rect x="6" y="2" width="32" height="26"/><circle cx="22" cy="15" r="7"/><path d="M20 12l5 3-5 3z M16 34h12M22 28v6"/></svg>Website<br>Design &amp;<br>Development</div>
    <div class="service"><svg width="44" height="40" viewBox="0 0 44 40" fill="none" stroke="#fff" stroke-width="1.5"><path d="M22 4l10 14-10 18-10-18z M22 4v16"/><circle cx="22" cy="20" r="3"/><path d="M4 6h10M30 6h10"/></svg>Graphic &amp;<br>Publication<br>Design</div>
    <div class="service"><svg width="44" height="40" viewBox="0 0 44 40" fill="none" stroke="#fff" stroke-width="1.5"><rect x="13" y="2" width="18" height="34" rx="3"/><circle cx="22" cy="14" r="5"/><path d="M19 30h6"/></svg>Pay Per Click<br>(Ppc)<br>Management</div>
    <div class="service"><svg width="44" height="40" viewBox="0 0 44 40" fill="none" stroke="#fff" stroke-width="1.5"><rect x="8" y="6" width="28" height="30"/><circle cx="22" cy="16" r="6"/><path d="M14 28h16M14 32h16M18 2h8v4"/></svg>Search<br>Engine<br>Optimization</div>
    <div class="service"><svg width="44" height="40" viewBox="0 0 44 40" fill="none" stroke="#fff" stroke-width="1.5"><circle cx="22" cy="10" r="6"/><circle cx="10" cy="28" r="6"/><circle cx="34" cy="28" r="6"/><path d="M18 15l-5 8M26 15l5 8M16 28h12"/></svg>Social<br>Media<br>Management</div>
    <div class="service"><svg width="44" height="40" viewBox="0 0 44 40" fill="none" stroke="#fff" stroke-width="1.5"><rect x="4" y="2" width="36" height="26"/><rect x="10" y="8" width="24" height="14"/><path d="M19 11l6 4-6 4z M16 34h12M22 28v6"/></svg>Video<br>Production &amp;<br>Editing</div>
    <div class="service"><svg width="44" height="40" viewBox="0 0 44 40" fill="none" stroke="#fff" stroke-width="1.5"><rect x="6" y="2" width="32" height="24"/><ellipse cx="24" cy="16" rx="8" ry="3"/><path d="M16 16v14c0 2 16 2 16 0V16M16 23c0 2 16 2 16 0"/></svg>Website<br>Hosting &amp;<br>Management</div>
    <div class="service"><svg width="44" height="40" viewBox="0 0 44 40" fill="none" stroke="#fff" stroke-width="1.5"><rect x="4" y="4" width="32" height="24"/><path d="M2 32h40M10 12h14M10 18h12M28 22l12-14"/></svg>Content<br>Creation And<br>Marketing</div>
  </div>
</section>

<div class="abs feature-photo" role="img" aria-label="Two desktop monitors on a wooden desk showing website layouts, with a plant beside them"></div>
<article class="abs feature-card">
  <h3>Website Design &amp; Development</h3>
  <p>Visitors won't spend more than 2 seconds waiting for your website to load. If it doesn't, they will click away</p>
  <p>Websites which don't have a clear layout and structure and are difficult to navigate can drive away potential customers.</p>
  <span class="btn">LEARN MORE<span class="knob"><svg width="14" height="14" viewBox="0 0 14 14"><path d="M7 1v12M2 6l5-5 5 5" fill="none" stroke="#ff4f0f" stroke-width="2"/></svg></span></span>
</article>

<div class="abs blog-title"><h2 class="section-title">BLOG <span>POST</span></h2></div>

<article class="abs post" style="left:162px">
  <div class="thumb" role="img" aria-label="Notebook with wireframe sketches and a pen on a desk" style="background:linear-gradient(135deg,#e9e7e2,#b9b3a8 60%,#6e4a36)"><div class="date">23<small>July</small></div></div>
  <h4>Lorem Ipsum is simply The dummy is Text Print Type Industry.</h4>
  <p>Lorem Ipsum is simply dummy text of the printing and typesetting the industry. Lorem Ipsum has been the industry's standard Lorem Ipsum is simply dummy.</p>
  <div class="rule"></div>
</article>
<article class="abs post" style="left:465px">
  <div class="thumb" role="img" aria-label="Laptop keyboard, camera lens and smartphone on a dark desk" style="background:linear-gradient(135deg,#cfd0d0,#6f7275 55%,#2b2c2e)"><div class="date">23<small>July</small></div></div>
  <h4>Lorem Ipsum is simply The dummy is Text Print Type Industry.</h4>
  <p>Lorem Ipsum is simply dummy text of the printing and typesetting the industry. Lorem Ipsum has been the industry's standard Lorem Ipsum is simply dummy.</p>
  <div class="rule"></div>
</article>
<article class="abs post" style="left:768px">
  <div class="thumb" role="img" aria-label="Hands holding a smartphone and a payment card for online shopping" style="background:linear-gradient(135deg,#8a8f93,#4a4d52 55%,#1f2124)"><div class="date">23<small>July</small></div></div>
  <h4>Lorem Ipsum is simply The dummy is Text Print Type Industry.</h4>
  <p>Lorem Ipsum is simply dummy text of the printing and typesetting the industry. Lorem Ipsum has been the industry's standard Lorem Ipsum is simply dummy.</p>
  <div class="rule"></div>
</article>

<div class="abs contact-photo" role="img" aria-label="Person working on a laptop while sitting on a grey sofa"></div>
<div class="abs talk-circle"></div>
<div class="abs talk-title">LET'S <span>TALK</span></div>
<div class="abs field" style="top:3350px;height:33px">Enter Name</div>
<div class="abs field" style="top:3396px;height:32px">Enter Email</div>
<div class="abs field" style="top:3440px;height:32px">Enter Contact No.</div>
<div class="abs field" style="top:3485px;height:78px">Enter Message</div>
<span class="abs btn talk-btn">SEND MESSAGE<span class="knob"><svg width="14" height="14" viewBox="0 0 14 14"><path d="M7 1v12M2 6l5-5 5 5" fill="none" stroke="#ff4f0f" stroke-width="2"/></svg></span></span>

<svg class="abs footer-wave" width="1200" height="80" viewBox="0 0 1200 80">
  <path d="M0 72 L600 40 L1200 0 L1200 80 L0 80Z" fill="#ff4f0f"/>
  <path d="M0 80 L600 58 L1200 42 L1200 80Z" fill="#070707"/>
</svg>
<footer class="abs footer">
  <div class="f-brand"><span class="dot"></span><span class="name">SUMMIT DIGITAL</span></div>
  <p class="about">Lorem Ipsum is simply dummy text of the printing and typesetting the industry. Lorem Ipsum has been the industry'.</p>
  <div class="socials"><span></span><span></span><span></span><span></span></div>
  <div class="f-col" style="left:466px">
    <h5>SITEMAP</h5>
    <ul><li>Home</li><li>About</li><li>Services</li><li>Testimonials</li><li>Contact Us</li></ul>
  </div>
  <div class="f-col" style="left:770px">
    <h5>CONTACT US</h5>
    <ul class="contact-list">
      <li><svg width="14" height="18" viewBox="0 0 14 18"><path d="M7 17S1 10 1 6.5a6 6 0 0112 0C13 10 7 17 7 17z" fill="none" stroke="#ff4f0f" stroke-width="1.5"/><circle cx="7" cy="6.5" r="2" fill="#ff4f0f"/></svg><span>SUMMIT DIGITAL<br>101 – lorem ipsum simple<br>text print.</span></li>
      <li><svg width="14" height="14" viewBox="0 0 24 24"><path d="M6.6 10.8a15 15 0 006.6 6.6l2.2-2.2c.3-.3.7-.4 1-.2 1.1.4 2.3.6 3.6.6.6 0 1 .4 1 1V20c0 .6-.4 1-1 1A17 17 0 013 4c0-.6.4-1 1-1h3.5c.6 0 1 .4 1 1 0 1.3.2 2.5.6 3.6.1.3 0 .7-.2 1z" fill="#ff4f0f"/></svg><span>(+1) 123 456 7890</span></li>
      <li><svg width="14" height="11" viewBox="0 0 13 10"><rect x="0" y="0" width="13" height="10" fill="#ff4f0f"/><path d="M0 0l6.5 5L13 0" fill="none" stroke="#070707"/></svg><span>info@summitdigitalhq.com</span></li>
    </ul>
  </div>
  <div class="copyright">©SUMMIT DIGITAL - 2020 All rights reserved.</div>
</footer>

</body>
</html>
```